Rural contractor needs professional informative business card

We need a business card design that looks professional but also includes information about the services that the business offers.
The business is an earthmoving and transport business. All of the services offered are listed on the old card attached.
The business is aimed at farmers so the design we are after is a classic look. The card needs to include all of the information that is listed on the old card design uploaded as an attachment. We recognize that this is a lot of information to fit on a business card but it also operates as a key marketing tool so is very important to the business.
Feel free to send me your questions.
Thanks
Reason: We are having trouble deciding between all these great designs - thank you for your efforts
We would love to see some designs using red with a little white and black. Also feel free to re-design our logo if you feel it needs to be to fit your designs. Thank you

```html
<!DOCTYPE html>
<html lang="en">
<head>
<meta charset="utf-8">
<title>RB Callister Contracting – Business Card</title>
<link href="https://fonts.googleapis.com/css2?family=Marcellus&family=Questrial&display=swap" rel="stylesheet">
<style>
  :root {
    --stage: #1b1b1b;
    --cream: #f4efd9;
    --sand: #e3d7a8;
    --gold: #b9a157;
    --gold-deep: #8f7b3a;
    --olive: #6f6330;
    --ink: #141414;
    --text: #2b2a24;
    --sepia-light: #d9cfa6;
    --sepia-dark: #8d8055;
  }
  * { box-sizing: border-box; margin: 0; padding: 0; }
  html, body { width: 1200px; height: 871px; overflow: hidden; background: var(--stage); }
  body { position: relative; font-family: 'Questrial', sans-serif; }

  .card {
    position: absolute;
    width: 640px; height: 366px;
    overflow: hidden;
    border-radius: 3px;
  }

  /* ---------- Back of card ---------- */
  .card-back { left: 60px; top: 50px; background: var(--sepia-light); }
  .back-photo {
    position: absolute; inset: 0 0 110px 0;
    background: linear-gradient(180deg, #efe9cf 0%, #d6cb9e 45%, #a89a66 100%);
  }
  .back-heading {
    position: absolute; left: 40px; right: 40px; top: 218px;
    display: flex; justify-content: space-between;
    font-size: 19px; letter-spacing: 3px; color: var(--ink);
  }
  .back-services {
    position: absolute; left: 0; right: 0; bottom: 0; height: 110px;
    background: linear-gradient(180deg, var(--olive) 0%, var(--gold-deep) 60%, var(--gold) 100%);
    display: grid; grid-template-columns: 1fr 1fr;
    padding: 16px 40px; column-gap: 30px;
  }
  .back-services ul { list-style: none; }
  .back-services li {
    font-size: 14px; letter-spacing: 1.5px; line-height: 21px; color: var(--cream);
  }

  /* ---------- Front of card ---------- */
  .card-front {
    left: 500px; top: 455px;
    background: linear-gradient(100deg, var(--sand) 0%, #ece4c3 45%, var(--cream) 75%, #f3efe6 100%);
  }
  .front-photo {
    position: absolute; left: 300px; top: 110px; width: 340px; height: 256px;
    background: linear-gradient(90deg, rgba(200,185,130,0) 0%, #c7b98a 25%, #a99d7e 60%, #8f8a7c 100%);
  }
  .brand {
    position: absolute; left: 40px; top: 26px;
    display: flex; align-items: center; gap: 10px;
    font-size: 26px; color: var(--ink); letter-spacing: 0.5px;
  }
  .brand-mark { width: 12px; height: 12px; background: var(--ink); }
  .name-band {
    position: absolute; left: 0; top: 92px; width: 400px; height: 30px;
    background: linear-gradient(90deg, var(--gold) 0%, #cdb976 55%, rgba(205,185,118,0) 100%);
  }
  .name {
    position: absolute; left: 56px; top: 97px;
    font-family: 'Marcellus', serif; font-size: 17px; letter-spacing: 2.5px;
    color: var(--ink); text-transform: uppercase;
  }
  .address {
    position: absolute; left: 56px; top: 138px;
    font-size: 13px; line-height: 19px; letter-spacing: 1.5px; color: var(--text);
  }
  .contact {
    position: absolute; left: 30px; top: 196px;
    font-size: 13px; letter-spacing: 1.5px; color: var(--text);
  }
  .contact-row { display: flex; align-items: center; gap: 14px; height: 22px; }
  .contact-row svg { width: 12px; height: 12px; }
  .footer-band { position: absolute; left: 0; bottom: 0; width: 640px; height: 110px; }
  .tagline {
    position: absolute; left: 120px; bottom: 36px;
    font-size: 17px; letter-spacing: 3.5px; color: var(--gold);
  }
</style>
</head>
<body>

  <section class="card card-back" aria-label="Card back">
    <div class="back-photo" role="img" aria-label="Sepia photograph of a road grader working in a paddock"></div>
    <div class="back-heading"><span>Earthmoving &amp;</span><span>Transport</span></div>
    <div class="back-services">
      <ul>
        <li>Road Building &amp; Maintenance</li>
        <li>Poly Pipe Laying</li>
        <li>Clearing Fence Lines</li>
        <li>Sand &amp; Gravel Supply</li>
      </ul>
      <ul>
        <li>Channel &amp; Drain Work</li>
        <li>Gravel Carting</li>
      </ul>
    </div>
  </section>

  <section class="card card-front" aria-label="Card front">
    <div class="front-photo" role="img" aria-label="Photograph of a prime mover hauling round cotton bales"></div>

    <div class="brand"><span class="brand-mark"></span><span>RB Callister Contracting</span></div>

    <div class="name-band"></div>
    <div class="name">Rowan Callister</div>

    <address class="address" style="font-style:normal">
      42 Tarwin Street<br>Dunmore 2864
    </address>

    <div class="contact">
      <div class="contact-row">
        <svg viewBox="0 0 12 12" aria-hidden="true"><path d="M2 1h2l1 3-1.5 1a7 7 0 0 0 3.5 3.5L8 7l3 1v2a1 1 0 0 1-1 1A9 9 0 0 1 1 2a1 1 0 0 1 1-1z" fill="#2b2a24"/></svg>
        <span>0400 555 218</span>
      </div>
      <div class="contact-row">
        <svg viewBox="0 0 12 12" aria-hidden="true"><rect x="0.75" y="2.25" width="10.5" height="7.5" fill="none" stroke="#2b2a24" stroke-width="1.2"/><path d="M1 2.5l5 4 5-4" fill="none" stroke="#2b2a24" stroke-width="1.2"/></svg>
        <span>rowan@callisterworks.com</span>
      </div>
    </div>

    <svg class="footer-band" viewBox="0 0 640 110" aria-hidden="true">
      <path d="M0 110 V92 H640 V110 Z" fill="var(--gold)"/>
      <path d="M0 92 V50 C0 20 25 4 70 4 H530 C560 4 575 20 575 50 V92 Z" fill="var(--ink)"/>
    </svg>
    <div class="tagline">Earthmoving &amp; Transport Solutions</div>
  </section>

</body>
</html>
```